Talent Management Company needs an Employee Engagement Infographic

We need an interesting 1 page infographic that will help us to quickly and clearly share with clients the benefits Employee Engagement will have on their company's bottom line and culture.

You may get an idea of our brand and colors by visiting brightquorel.com
We are a Talent Management Solutions company that specializes in helping our clients become great places to work with a strong focus on culture.

Attached is the information that should be included. We would like it to be on 1 page if possible. There is a lot of information attached, but it may be bulleted, shown with charts, graphics, etc.

Industry/Entity Type

It Company

```html
<!DOCTYPE html>
<html lang="en">
<head>
<meta charset="utf-8">
<title>Employee Engagement Infographic</title>
<link href="https://fonts.googleapis.com/css2?family=Questrial&family=Roboto+Slab:wght@300;400;700&display=swap" rel="stylesheet">
<style>
  :root{
    --orange:#f2a72a;
    --ink:#3f3f3f;
    --blue:#1b9ad6;
    --band:#dedede;
    --map:#fdecc8;
    --page:#ffffff;
    --backdrop:#efefef;
  }
  *{box-sizing:border-box;margin:0;padding:0}
  html,body{width:1000px;height:1200px;overflow:hidden;background:var(--backdrop)}
  .stage{position:relative;width:1000px;height:1200px;font-family:"Roboto Slab",serif;font-weight:300;color:var(--ink)}
  .abs{position:absolute}
  .sheet{left:88px;top:18px;width:824px;height:1162px;background:var(--page)}
  .header-band{left:88px;top:18px;width:824px;height:147px;background:var(--band)}
  .brand{left:140px;top:45px;width:110px;height:110px;border-radius:50%;background:var(--page);display:flex;align-items:center;justify-content:center;font-family:"Questrial",sans-serif;font-size:15px;color:var(--ink)}
  .heading{font-family:"Questrial",sans-serif;color:var(--orange);font-size:24px;font-weight:400;white-space:nowrap}
  .quote{font-size:14px;line-height:19px}
  .rule{border-top:2px dotted var(--orange);height:0}
  .vrule{border-left:2px dotted var(--orange);width:0}
  .stat{font-size:12.5px;line-height:16px}
  .stat .big{font-family:"Questrial",sans-serif;color:var(--orange);font-size:19px}
  .map-area{left:175px;top:385px;width:380px;height:250px;background:var(--map);border-radius:40px 90px 60px 30px}
  .hero-figure{left:146px;top:452px;font-family:"Roboto Slab",serif;font-weight:700;color:var(--orange);font-size:82px;line-height:1}
  .hero-caption{left:152px;top:541px;font-size:14px;line-height:17px}
  .segment{width:62px;height:62px;border-radius:50%;background:var(--orange);outline:2px dotted var(--orange);outline-offset:4px;display:flex;align-items:center;justify-content:center;text-align:center;font-family:"Questrial",sans-serif;font-size:13px;line-height:15px;color:var(--ink)}
  .segment-value{font-family:"Questrial",sans-serif;color:var(--orange);font-size:32px}
  .definition{font-size:12px;line-height:16.5px;width:200px}
  .definition .term{font-family:"Questrial",sans-serif;color:var(--orange);font-size:20px}
  .lead{left:130px;top:660px;width:740px;font-size:14.5px;line-height:20px;font-weight:400}
  .icon-disc{width:52px;height:52px;border-radius:50%;background:var(--blue);outline:2px dotted var(--blue);outline-offset:3px}
  .checklist{left:197px;top:762px;list-style:none;font-size:12.5px;line-height:15px}
  .checklist li{position:absolute;left:0;display:flex;align-items:flex-start;width:270px}
  .checklist .box{flex:none;width:22px;height:22px;border:1.5px dashed var(--orange);margin-right:9px;margin-top:-4px}
  .checklist svg{display:block}
  .closing{left:130px;top:1068px;width:315px;text-align:center;font-size:18px;line-height:25px;font-weight:400}
  .closing .term{font-family:"Questrial",sans-serif;color:var(--orange);font-size:23px}
  .tactics{left:491px;top:727px;width:380px}
  .tactic{margin-bottom:10px}
  .tactic h3{font-family:"Questrial",sans-serif;color:var(--orange);font-weight:400;font-size:14px;line-height:17px}
  .tactic p{font-size:12.5px;line-height:16px}
</style>
</head>
<body>
<div class="stage">
  <div class="abs sheet"></div>
  <div class="abs header-band"></div>
  <div class="abs brand">brightquorel</div>

  <h1 class="abs heading" style="left:130px;top:178px">What is Employee Engagement?</h1>
  <p class="abs quote" style="left:130px;top:212px;width:740px">“The emotional and functional commitment an employee has to his or her organization”<br>- Harlan Whitcombe</p>
  <div class="abs rule" style="left:130px;top:260px;width:740px"></div>

  <h2 class="abs heading" style="left:130px;top:274px">Why Employers Engagement Matters?</h2>
  <svg class="abs" style="left:130px;top:305px" width="56" height="56" viewBox="0 0 56 56" aria-hidden="true">
    <circle cx="28" cy="28" r="26" fill="none" stroke="var(--blue)" stroke-width="2" stroke-dasharray="2 3"/>
    <circle cx="28" cy="28" r="22" fill="var(--blue)"/>
    <polyline points="16,36 25,27 30,32 39,20" fill="none" stroke="#fff" stroke-width="3.5" stroke-linejoin="round"/>
    <polyline points="33,19 40,19 40,26" fill="none" stroke="#fff" stroke-width="3.5"/>
  </svg>
  <p class="abs stat" style="left:196px;top:305px;width:215px">Companies with engaged employees outperform the competition by as much as <span class="big">202%</span> (Norwick Poll)</p>
  <div class="abs vrule" style="left:420px;top:305px;height:48px"></div>
  <p class="abs stat" style="left:432px;top:305px;width:215px">Encourages quality of product and/or service, improves retention, attracts top talent, <span class="big">drives profit</span></p>
  <div class="abs vrule" style="left:652px;top:305px;height:48px"></div>
  <p class="abs stat" style="left:662px;top:300px;width:215px"><span class="big">$11 Billion</span> are lost annually due to high turnover of employees (Office of Labor Metrics)</p>

  <div class="abs map-area" role="img" aria-label="Map of the United States"></div>
  <div class="abs hero-figure">71%</div>
  <p class="abs hero-caption">workers are unhappy<br>at their job</p>

  <svg class="abs" style="left:300px;top:440px" width="120" height="150" viewBox="0 0 120 150" aria-hidden="true">
    <defs><marker id="head" markerWidth="8" markerHeight="8" refX="7" refY="4" orient="auto"><path d="M0,0 L8,4 L0,8 z" fill="#444"/></marker></defs>
    <g stroke="#444" stroke-width="1.5" marker-end="url(#head)">
      <line x1="5" y1="65" x2="112" y2="8"/>
      <line x1="5" y1="75" x2="112" y2="75"/>
      <line x1="5" y1="85" x2="112" y2="140"/>
    </g>
  </svg>
  <div class="abs segment" style="left:447px;top:405px">Engaged</div>
  <div class="abs segment-value" style="left:528px;top:416px">29%</div>
  <div class="abs segment" style="left:447px;top:485px">Actively<br>Disengaged</div>
  <div class="abs segment-value" style="left:528px;top:496px">26%</div>
  <div class="abs segment" style="left:447px;top:565px">Not<br>Engaged</div>
  <div class="abs segment-value" style="left:528px;top:576px">45%</div>

  <p class="abs definition" style="left:670px;top:370px"><span class="term">Engaged</span> employees are more motivated, committed to their employer and likely to stay focused to help the business in achieving goals and driving the organization’s future. Employee engagement.</p>
  <div class="abs rule" style="left:670px;top:492px;width:200px"></div>
  <p class="abs definition" style="left:670px;top:503px"><span class="term">Disengaged</span> workers are emotionally disconnected from their workplace and less productive than engaged counterparts. They may drag down coworkers and impact everything from customer service to sales, quality, productivity, and employee retention.</p>

  <p class="abs lead">It’s not just about money.  Psychological and social satisfaction may determine which employees are motivated to stay, work hard, and help to build an organization’s success.</p>
  <div class="abs rule" style="left:130px;top:708px;width:740px"></div>

  <h2 class="abs heading" style="left:128px;top:722px">What Engages Employees?</h2>
  <div class="abs icon-disc" style="left:130px;top:761px"></div>

  <ul class="abs checklist">
    <li style="top:8px"><span class="box"><svg width="20" height="20" viewBox="0 0 20 20"><polyline points="3,10 8,15 17,4" fill="none" stroke="var(--orange)" stroke-width="2.5"/></svg></span>Relationship with Direct Manager</li>
    <li style="top:43px"><span class="box"><svg width="20" height="20" viewBox="0 0 20 20"><polyline points="3,10 8,15 17,4" fill="none" stroke="var(--orange)" stroke-width="2.5"/></svg></span>Faith in Leadership</li>
    <li style="top:78px"><span class="box"><svg width="20" height="20" viewBox="0 0 20 20"><polyline points="3,10 8,15 17,4" fill="none" stroke="var(--orange)" stroke-width="2.5"/></svg></span>Pride in what the company is doing</li>
    <li style="top:113px"><span class="box"><svg width="20" height="20" viewBox="0 0 20 20"><polyline points="3,10 8,15 17,4" fill="none" stroke="var(--orange)" stroke-width="2.5"/></svg></span>Financial Incentives</li>
    <li style="top:148px"><span class="box"><svg width="20" height="20" viewBox="0 0 20 20"><polyline points="3,10 8,15 17,4" fill="none" stroke="var(--orange)" stroke-width="2.5"/></svg></span>Rewards and Recognition</li>
    <li style="top:184px"><span class="box"><svg width="20" height="20" viewBox="0 0 20 20"><polyline points="3,10 8,15 17,4" fill="none" stroke="var(--orange)" stroke-width="2.5"/></svg></span>Social connections</li>
    <li style="top:214px"><span class="box"><svg width="20" height="20" viewBox="0 0 20 20"><polyline points="3,10 8,15 17,4" fill="none" stroke="var(--orange)" stroke-width="2.5"/></svg></span>Involvement in important decisions<br>and processes</li>
    <li style="top:255px"><span class="box"><svg width="20" height="20" viewBox="0 0 20 20"><polyline points="3,10 8,15 17,4" fill="none" stroke="var(--orange)" stroke-width="2.5"/></svg></span>Effective communication</li>
  </ul>

  <div class="abs rule" style="left:130px;top:1056px;width:315px"></div>
  <p class="abs closing"><span class="term">Engaged</span> employees are Enthusiastic, Empowered, Inspired, and Confident!</p>

  <div class="abs tactics">
    <div class="tactic"><h3>What are employees thinking</h3><p>Listen to the employees – community forums, surveys, suggestion box, open-door policy</p></div>
    <div class="tactic"><h3>Create a culture</h3><p>Build a community, allow employees to feel comfortable and part of something bigger</p></div>
    <div class="tactic"><h3>Show appreciation for impacts big and small</h3><p>Rewards, recognition, appreciation, acknowledge good work</p></div>
    <div class="tactic"><h3>Open, honest communication</h3><p>Show employees why what they do is so important</p></div>
    <div class="tactic"><h3>Career path development</h3><p>Show employees where they can go and how they can get there – help them envision their future</p></div>
    <div class="tactic"><h3>Interactions outside work</h3><p>Community outreach projects, organization wide celebrations/parties</p></div>
    <div class="tactic"><h3>Tell the organization’s story</h3><p>Strong employment branding, what does the company set out to accomplish</p></div>
  </div>
</div>
</body>
</html>
```